Résumé app needs 1 more template

Hi, I need 1 more template for my résumé app. The résumé app can be used in a browser (https://paperloom.com/resume-app) on an Nexor / Tabbo (https://apps.marlowstore.com/app/id530218746) or on an Veltrix (https://get.brinkmarket.com/store/apps/details?id=com.paperloom.resume). The app lets the user create a résumé. It currently let's the user choose between 3 templates. I need 1 more. Please use the app first so you know how it will work.

Target Market(s)

Users of the app

Colors

Requirements
Must have
• original
• beautiful
• the resume template contains the data that the user can currently enter in the app (so do NOT design new features like sliders for level of experience etc)

```html
<!DOCTYPE html>
<html lang="en">
<head>
<meta charset="utf-8">
<title>Résumé Template</title>
<link rel="stylesheet" href="https://fonts.googleapis.com/css2?family=Marcellus+SC&display=swap">
<style>
  :root {
    --band-blue: #cdeeff;
    --paper: #f7f7f6;
    --paper-light: #ffffff;
    --name-grey: #6e6e6e;
    --heading-grey: #5f5f5f;
    --body-grey: #9a9a9a;
    --photo-warm: #b27a5c;
    --photo-cool: #7f97a6;
  }
  * { margin: 0; padding: 0; box-sizing: border-box; }
  html, body { width: 849px; height: 1200px; overflow: hidden; }
  body { font-family: "Marcellus SC", serif; background: var(--paper-light); }
  .resume {
    position: relative; width: 849px; height: 1200px; overflow: hidden;
    background: linear-gradient(160deg, var(--paper) 0%, var(--paper-light) 45%, #f1f1f1 62%, var(--paper-light) 80%);
  }
  .backdrop-texture {
    position: absolute; left: 0; top: 240px; width: 849px; height: 960px;
    background: linear-gradient(125deg, transparent 35%, rgba(200,200,200,0.18) 50%, transparent 65%);
  }
  .header-band {
    position: absolute; left: 0; top: 0; width: 849px; height: 240px;
    background: var(--band-blue);
  }
  .portrait {
    position: absolute; left: 13px; top: 9px; width: 222px; height: 222px; border-radius: 50%;
    background: radial-gradient(circle at 50% 40%, var(--photo-warm) 0%, #8d6a58 40%, var(--photo-cool) 75%, #cfe2ea 100%);
  }
  .name {
    position: absolute; left: 266px; top: 52px; width: 510px; text-align: center;
    font-size: 64px; font-weight: 400; color: var(--name-grey); letter-spacing: 2px; line-height: 1;
  }
  .contact {
    position: absolute; left: 266px; top: 135px; width: 510px; text-align: center;
    font-size: 28px; color: var(--name-grey); letter-spacing: 1px; line-height: 1;
  }
  .section { position: absolute; left: 57px; width: 728px; }
  .section-title {
    font-size: 32px; font-weight: 400; color: var(--heading-grey); letter-spacing: 1px; line-height: 1; margin-bottom: 12px;
  }
  .section-body {
    font-size: 16.5px; color: var(--body-grey); line-height: 21.8px; text-align: justify; text-align-last: justify;
    letter-spacing: 0.3px; overflow: hidden;
  }
  .about { top: 310px; }
  .experience { top: 560px; }
  .education { top: 678px; }
  .extra { top: 796px; }
  .lines-8 { height: 174.4px; }
  .lines-2 { height: 43.6px; }
  .footer-wave { position: absolute; left: 0; bottom: 0; width: 849px; height: 120px; }
</style>
</head>
<body>
<main class="resume">
  <div class="backdrop-texture" role="img" aria-label="Soft faded photograph of a fountain pen on white paper"></div>

  <header class="header-band">
    <div class="portrait" role="img" aria-label="Circular portrait photo of the résumé owner"></div>
    <h1 class="name">Name Surname</h1>
    <p class="contact">Phone / e-mail / address</p>
  </header>

  <section class="section about">
    <h2 class="section-title">About you</h2>
    <p class="section-body lines-8">Lorem Ipsum Lorem Ipsum lorem ipsum lorem ipsum Lorem Ipsum lorem Ipsum lorem ipsum lorem ipsum Lorem Ipsum lorem ipsum lorem ipsum lorem Ipsum Lorem Ipsum lorem ipsum lorem ipsum lorem ipsum lorem Ipsum lorem Ipsum lorem ipsum lorem ipsum lorem ipsum lorem ipsum Lorem Ipsum Lorem ipsum Lorem Ipsum lorem ipsum lorem ipsum lorem ipsum lorem Ipsum lorem ipsum Lorem ipsum lorem ipsum Lorem Ipsum lorem ipsum Lorem Ipsum lorem ipsum lorem Ipsum Lorem Ipsum lorem ipsum lorem ipsum lorem ipsum Lorem Ipsum lorem ipsum lorem ipsum Lorem Ipsum lorem ipsum lorem Ipsum lorem ipsum lorem ipsum lorem ipsum lorem Ipsum lorem ipsum lorem ipsum lorem ipsum.</p>
  </section>

  <section class="section experience">
    <h2 class="section-title">Expirience</h2>
    <p class="section-body lines-2">lorem ipsum lorem ipsum lorem ipsum Lorem Ipsum lorem ipsum lorem ipsum lorem ipsum Lorem Ipsum lorem ipsum lorem ipsum lorem ipsum Lorem Ipsum lorem ipsum Lorem Ipsum lorem ipsum Lorem Ipsum lorem ipsum lorem ipsum lorem ipsum lorem Ipsum.</p>
  </section>

  <section class="section education">
    <h2 class="section-title">Education</h2>
    <p class="section-body lines-2">lorem ipsum lorem ipsum lorem ipsum Lorem Ipsum lorem ipsum lorem ipsum lorem ipsum lorem ipsum lorem ipsum lorem ipsum lorem ipsum lorem ipsum lorem ipsum lorem ipsum Lorem Ipsum lorem ipsum lorem ipsum Lorem Ipsum lorem ipsum lorem Ipsum.</p>
  </section>

  <section class="section extra">
    <h2 class="section-title">Something else</h2>
    <p class="section-body lines-8">Lorem ipsum lorem ipsum lorem ipsum Lorem Ipsum lorem ipsum lorem ipsum lorem ipsum lorem ipsum lorem ipsum lorem ipsum Lorem ipsum Lorem Ipsum lorem ipsum Lorem Ipsum lorem ipsum lorem ipsum lorem ipsum lorem ipsum lorem ipsum lorem ipsum Lorem Ipsum Lorem Ipsum Lorem Ipsum lorem ipsum lorem ipsum Lorem Ipsum lorem ipsum lorem ipsum lorem ipsum lorem ipsum Lorem Ipsum lorem ipsum lorem ipsum lorem ipsum lorem ipsum lorem ipsum lorem ipsum Lorem ipsum lorem ipsum lorem ipsum lorem ipsum lorem Ipsum lorem ipsum lorem ipsum lorem ipsum lorem ipsum lorem ipsum Lorem Ipsum lorem ipsum lorem Ipsum lorem ipsum lorem ipsum lorem ipsum lorem ipsum lorem ipsum lorem ipsum Lorem Ipsum lorem ipsum lorem ipsum.</p>
  </section>

  <svg class="footer-wave" viewBox="0 1080 849 120" preserveAspectRatio="none" aria-hidden="true">
    <path d="M0 1090 C60 1150 120 1168 200 1164 C380 1150 520 1085 660 1088 C760 1090 820 1110 849 1124 L849 1200 L0 1200 Z" fill="var(--band-blue)"/>
  </svg>
</main>
</body>
</html>
```